Local Mortgage Broker requires DL Flyer

I Require DL sized design for local mortgage broker. Content that will go on the flyer is attached along with the logo.
Looking for a bright & catchy design with that little OOMPH.....on the creative side.
Am looking for a responsive campaign with this style of marketing. The main message is that "We may be able to save thousands of dollars for you, just give us a chance to review your mortgages"

Target Market(s)

All home owners with a mortgage or eople looking to buy their first home.

Industry/Entity Type

Marketing

```html
<!DOCTYPE html>
<html lang="en">
<head>
<meta charset="utf-8">
<title>HomeLend Co – Switch Over Reward Flyer</title>
<link href="https://fonts.googleapis.com/css2?family=Oswald:wght@700&family=Roboto+Condensed:wght@700&family=Roboto:wght@400;700&display=swap" rel="stylesheet">
<style>
  :root {
    --navy: #2a2863;
    --slate: #6a6b6e;
    --shadow-grey: #c9cacc;
    --ink: #1d1d1f;
    --white: #ffffff;
    --bar-text: #e4e4ea;
    --backdrop: #75777b;
  }
  * { box-sizing: border-box; margin: 0; padding: 0; }
  html, body {
    width: 1200px; height: 636px; overflow: hidden;
    background: var(--backdrop);
  }
  .flyer {
    position: absolute; left: 62px; top: 62px;
    width: 1078px; height: 510px;
    background: var(--white);
    overflow: hidden;
  }
  .hero-photo {
    position: absolute; left: 478px; top: 0;
    width: 600px; height: 370px;
    background:
      radial-gradient(ellipse at 30% 70%, #d9dde3 0%, rgba(217,221,227,0) 45%),
      radial-gradient(ellipse at 75% 35%, #eceae8 0%, rgba(236,234,232,0) 55%),
      linear-gradient(135deg, #f4f4f4 0%, #e2e4e8 50%, #f7f7f7 100%);
    -webkit-mask-image: linear-gradient(to bottom, #000 70%, transparent 100%);
            mask-image: linear-gradient(to bottom, #000 70%, transparent 100%);
  }
  .offer-amount {
    position: absolute; left: 36px; top: 7px;
    display: flex; align-items: baseline;
    font: 700 180px/1 "Oswald", sans-serif;
    letter-spacing: -2px;
    color: var(--navy);
    text-shadow: 6px 5px 0 var(--shadow-grey);
    white-space: nowrap;
  }
  .offer-amount .currency {
    font-size: 148px;
    margin-right: 2px;
  }
  .offer-lead {
    position: absolute; left: 38px; top: 21px;
    z-index: 2;
    font: 700 27px/1 "Roboto Condensed", sans-serif;
    color: var(--navy);
  }
  .headline {
    position: absolute; left: 40px; top: 197px;
    font: 700 51px/50px "Roboto Condensed", sans-serif;
    color: var(--slate);
    text-transform: uppercase;
  }
  .subline {
    position: absolute; left: 40px; top: 305px;
    font: 700 20px/24px "Roboto", sans-serif;
    color: var(--navy);
    text-transform: uppercase;
  }
  .fine-print {
    position: absolute; left: 40px; top: 371px;
    font: 400 15px/20px "Roboto", sans-serif;
    color: var(--ink);
    white-space: nowrap;
  }
  .fine-print strong { font-weight: 700; }
  .brand {
    position: absolute; left: 812px; top: 392px;
    display: flex; align-items: center; gap: 10px;
    font: 700 34px/1 "Roboto", sans-serif;
    color: var(--navy);
  }
  .brand-mark {
    width: 22px; height: 22px; background: var(--navy);
  }
  .contact-bar {
    position: absolute; left: 0; bottom: 0;
    width: 100%; height: 62px;
    background: var(--navy);
    display: flex; justify-content: center; align-items: center;
    font: 700 32px/1 "Roboto Condensed", sans-serif;
    color: var(--bar-text);
    letter-spacing: 0.5px;
  }
  .contact-bar .divider {
    width: 2px; height: 30px; background: var(--bar-text);
    margin: 0 18px;
  }
</style>
</head>
<body>
  <main class="flyer">
    <div class="hero-photo" role="img" aria-label="Photo of a model house beside a woman signing mortgage papers with a pen and house keys on the desk"></div>

    <div class="offer-amount"><span class="currency">$</span><span>3000</span></div>
    <div class="offer-lead">Upto</div>

    <h1 class="headline">Get rewarded by<br>switching over.</h1>

    <p class="subline">Get up to $3000 voucher or cash back*<br>on the settlement of your loan.</p>

    <p class="fine-print">*based on the size of the loan, You get upto 0.3% of your &nbsp;total loan settled through us.<br>For example a refinance of <strong>$600,000</strong> mortgage to any of our panel lenders will get you<br><strong>$ 0.30%</strong> of the $600,000, which is <strong>$1,800</strong> as your bonus/ reward,</p>

    <div class="brand"><span class="brand-mark"></span>HomeLend Co</div>

    <footer class="contact-bar">
      <span>CALL NOW</span>
      <span class="divider"></span>
      <span>0400 000 123</span>
      <span class="divider"></span>
      <span>WWW.HOMELENDCO.COM.AU</span>
    </footer>
  </main>
</body>
</html>
```